Landing page and nested content pages for HillsideFaithful.com

Web design for existing site https://hillsidefaithful.example/

This is a RESPONSIVE web site that needs to work on a medium-res mobile device and also look great on a widescreen desktop.

There are three or four public pages we currently have that need a fresh design, which will be used somewhat to guide the design direction for the non-public interior site for logged-in users in a later design effort.

The recently created new logo is attached and the new design should be based on this logo, I don't know how you'll do it, but the new logo should fit appropriately; the current web site's little logo on the top left must be thrown out, and one of our goals in this design effort is to set up the top nav bar, logo placement, etc. There are multiple logos attached to this project but the primary one to try for is the red door one. The other logos (gray+red arc logo and tree logo) are there in case you as the designer prefer them and can demonstrate that they are more suited for a web design than the red one. Otherwise I am hoping to see the red logo used for the site overall and the other logos to highlight discipleship and/or fellowship sections on the site.

The main pages are: 1) landing page, which describes the function of the site for logged-in users (not actually a part of this design project but the logged-in users' site redesign should be inspired by this effort) with multiple bits of content embedded on the page, and 2) a content page called "The Essentials" which contains several pages worth of content. The content is currently just a wall of text; it needs to be somehow broken down into clickable sections and imagery applied to make it interesting. 3) We also have some more minor pages which I'll list below.

The Landing Page

This is to redesign the content at https://hillsidefaithful.example/
The current web site's placeholder content represents the general direction desired for the landing page, but I'm not a designer, so colors and layout etc can be totally re-thought. I'd like to use these images and these highlights. I've uploaded the stock images.

The web site on the whole for logged-in users (again, not itself a part of this design) is part social network and part library of various guides and resources. So the landing page needs to highlight the objectives of the site while demonstrating some of the features of the site. There is currently also some additional text content that should also be there, but should not be so prominently displayed as it is today; it should be accessible from some scrolling and/or from a button-click pop-over, so that new visitors are not inundated with a wall of text. Besides the logo, I've uploaded some features of the site that might be useful in graphically highlighting the features of the site.

'The Essentials' Content Page

This is to redesign the content at https://hillsidefaithful.example/Gospel

The content at this URL is currently one big wall of text, and it is intimidating enough that people may not be likely to read it. It needs to be read.

Other minor content pages

We also have these pages that needs to demonstrate a "theme" of basic content pages' design strategy for basic content:

https://hillsidefaithful.example/freebibleresponse
and
https://hillsidefaithful.example/bibledistribution

We will be adding additional content pages later, but we need to finalize the design theme before proceeding.

As currently demonstrated, I tend to prefer a serif font for headings (for theming around ancient-yet-current faith-based content), sans-serif for paragraphs (for readability), which is why the current site uses the fonts it has. Find some better fonts as you please.

The images prefixed with "interior-features-" are for landing page reference only, you might choose to highlight a cropped snippet, but don't go too crazy since these features will themselves be redesigned and so we will need to replace whatever cropped sample you might use with another one later.

There will be login and register functions. I DO NOT want any of this functionality to be built, but I do want the core public-site UX concept built out with *CLEAN* and attractive markup in HTML+CSS(+JS?) based on Bootstrap 4.

Target Market(s)

Christians looking for fellowship and discipleship outside of traditional church buildings (in-home fellowship, online fellowship, online study resources)

• Landing page entices the user to register
'Essentials' page somehow redistributes content into meaningful sections
Other minor content pages are redesigned but not too complicated, so that future content pages can follow suit
Designer can choose the logo out of 3, but the red door logo was the preferred logo if you can work with it and integrate it into the site such as with a responsive site top nav bar logo
HTML+CSS must be clean and based on Bootstrap 4

```html
<!DOCTYPE html>
<html lang="en">
<head>
<meta charset="utf-8">
<title>HillsideFaithful.com</title>
<link href="https://fonts.googleapis.com/css2?family=Lora:wght@500;700&family=Roboto:wght@400;500;700&display=swap" rel="stylesheet">
<style>
:root{
  --red:#c4161c;
  --ink:#1f1f1f;
  --muted:#777;
  --light:#f6f6f6;
  --blue:#2d4060;
  --link:#2f7fd0;
  --black:#0b0b0b;
}
*{box-sizing:border-box;margin:0;padding:0}
html,body{width:1200px;height:3452px;overflow:hidden}
body{font-family:"Roboto",Arial,sans-serif;color:var(--ink);background:#fff;position:relative}
h1,h2,h3{font-family:"Lora",Georgia,serif;font-weight:700}
p{font-size:14px;line-height:1.65;color:var(--muted)}
.btn{display:inline-block;background:var(--red);color:#fff;font-size:13px;font-weight:500;padding:11px 22px;border-radius:3px;text-decoration:none}
.btn-outline{background:transparent;border:1px solid #fff}
.block{position:absolute;left:0;width:1200px}

/* header */
.site-header{top:0;height:108px;background:#fff;box-shadow:0 2px 8px rgba(0,0,0,.08);z-index:2}
.brand{position:absolute;left:180px;top:30px;display:flex;align-items:center;gap:10px;text-decoration:none}
.brand-mark{width:36px;height:36px;background:var(--red)}
.brand-name{font-family:"Roboto",sans-serif;font-weight:700;font-size:18px;color:var(--ink);letter-spacing:1px;text-transform:uppercase}
.account-links{position:absolute;right:180px;top:14px;font-size:12px;color:var(--red)}
.main-nav{position:absolute;right:180px;top:62px;display:flex;gap:30px;font-size:15px}
.main-nav a{color:var(--ink);text-decoration:none}
.main-nav a.active{color:var(--red);border-bottom:2px solid var(--red);padding-bottom:6px}

/* hero */
.hero{top:108px;height:492px;background:linear-gradient(100deg,#151515 0%,#2a2a2a 45%,#4a4540 70%,#2b2622 100%)}
.hero-content{position:absolute;left:180px;top:90px;width:420px}
.hero h1{color:#fff;font-size:44px;line-height:1.2}
.hero p{color:#d6d6d6;margin:22px 0 40px}

/* about */
.about{top:600px;height:520px}
.about-photo{position:absolute;left:32px;top:72px;width:508px;height:368px;background:linear-gradient(135deg,#6d5a48,#3b3631 60%,#8a7a68)}
.about-text{position:absolute;left:588px;top:92px;width:420px}
.section-title{font-size:34px;color:var(--ink)}
.lead{font-family:"Roboto",sans-serif;font-size:20px;font-weight:500;line-height:1.4;margin:22px 0 16px;color:var(--ink)}
.about-text p{margin-bottom:28px}
.about-text p a,.essentials-text p a{color:var(--link)}

/* essentials */
.essentials{top:1120px;height:428px}
.essentials-text{position:absolute;left:180px;top:40px;width:400px}
.essentials-text p{margin-bottom:28px}
.essentials-photo{position:absolute;left:640px;top:52px;width:348px;height:236px;background:linear-gradient(135deg,#b8dff0,#8ecbe6)}

/* banner */
.banner{top:1548px;height:232px;background:linear-gradient(180deg,#2d4262,#1f2f49);text-align:center;color:#fff}
.banner h2{font-size:34px;margin-top:40px;font-weight:500}
.banner p{color:#d0d7e3;width:620px;margin:14px auto 26px}

/* news */
.news{top:1780px;height:760px;background:var(--light)}
.news-head{position:absolute;left:180px;top:60px;width:840px}
.news-head .lead{width:380px}
.news-head p{width:520px}
.news-head .btn{position:absolute;right:0;top:150px}
.cards{position:absolute;left:180px;top:350px;display:flex;gap:20px}
.card{width:266px;height:380px;background:#fff;box-shadow:0 4px 14px rgba(0,0,0,.08)}
.card-photo{height:168px}
.card-body{padding:18px}
.card h3{font-family:"Roboto",sans-serif;font-size:16px;font-weight:700;margin-bottom:10px}
.card p{font-size:13px}
.read-more{display:block;margin-top:12px;font-size:13px;color:var(--link);text-decoration:none}

/* testimonial */
.testimonial{top:2540px;height:560px;text-align:center}
.testimonial h2{font-size:34px;margin-top:46px}
.testimonial .intro{width:560px;margin:12px auto 0}
.t-photo{position:absolute;left:288px;top:228px;width:192px;height:232px;background:linear-gradient(135deg,#c9b9a6,#6d5d50)}
.t-quote{position:absolute;left:640px;top:240px;width:330px;text-align:left}
.t-mark{position:absolute;left:580px;top:190px;font-family:"Lora",serif;font-size:200px;color:#eee;line-height:1}
.t-name{font-weight:700;font-size:14px;margin-top:20px;color:var(--ink)}
.t-role{font-size:12px;color:var(--muted)}
.arrow{position:absolute;top:318px;width:40px;height:40px;border-radius:50%;background:#fff;box-shadow:0 2px 10px rgba(0,0,0,.12);display:flex;align-items:center;justify-content:center}

/* footer */
.site-footer{top:3100px;height:352px;background:var(--black);color:#fff}
.f-brand{position:absolute;left:240px;top:56px;width:200px;text-align:center}
.f-brand .brand-name{color:#fff;font-size:17px}
.f-brand p{color:#ccc;font-size:12px;margin-top:14px}
.socials{display:flex;justify-content:center;gap:18px;margin-top:16px}
.socials span{width:12px;height:12px;border-radius:50%;background:#fff;display:block}
.f-col{position:absolute;top:64px}
.f-col h4{font-size:15px;font-weight:700;margin-bottom:20px}
.f-col li{list-style:none;font-size:13px;color:#ccc;margin-bottom:10px;display:flex;gap:8px;align-items:center}
.copyright{position:absolute;right:120px;bottom:24px;font-size:11px;color:#999}
</style>
</head>
<body>

<header class="block site-header">
  <a class="brand" href="#"><span class="brand-mark"></span><span class="brand-name">Hillside Faithful</span></a>
  <div class="account-links">Login | Register</div>
  <nav class="main-nav">
    <a class="active" href="#">Home</a><a href="#">About Us</a><a href="#">Essentials</a><a href="#">News</a><a href="#">Testimonies</a>
  </nav>
</header>

<section class="block hero" role="img" aria-label="Photo of a person seated with an open Bible on a table">
  <div class="hero-content">
    <h1>Discover God And His Presence</h1>
    <p>The main idea is a call to its early planning stages and what you currently see here are some somewhat functional resources pertaining to the larger objectives.</p>
    <a class="btn" href="#">Read More</a>
  </div>
</section>

<section class="block about">
  <div class="about-photo" role="img" aria-label="Photo of a group seated around a table with open Bibles"></div>
  <div class="about-text">
    <h2 class="section-title">About Us</h2>
    <div class="lead">Those objectives are primarily to encourage local believers</div>
    <p>Those objectives are primarily to encourage local believers in any neighborhood around the world to read the Bible, be followers first, and be present, become disciples, and make disciples, independently of or in complement to the purposes of the <a href="#">established church</a>.</p>
    <a class="btn" href="#">Learn More</a>
  </div>
</section>

<section class="block essentials">
  <div class="essentials-text">
    <h2 class="section-title">Essentials</h2>
    <div class="lead">Before we get started</div>
    <p>We use <a href="#">the Bible</a> as the basis for discussing Jesus and Christianity. The Bible is a compilation of 66 books, mostly originally in Hebrew and Greek, written over many centuries and inspired by the Holy Spirit. That is, we believe it presents the message God intends for every person.</p>
    <a class="btn" href="#">Explore</a>
  </div>
  <div class="essentials-photo" role="img" aria-label="Photo of a black Bible with a rosary on a light blue surface"></div>
</section>

<section class="block banner">
  <h2>Christian, meet Christian</h2>
  <p>This site means that this site intends to encourage Christian neighbors to discover and support one another as a network of believers, including in fellowship, in discipleship, and in practical support.</p>
  <a class="btn btn-outline" href="#">Join With Us</a>
</section>

<section class="block news">
  <div class="news-head">
    <h2 class="section-title">Recent News</h2>
    <div class="lead">We are hoping to be planting seeds and tilling soil</div>
    <p>We do all this for our many reasons. We want you to be with us because we need an invitation certain that everyone is the same.</p>
    <a class="btn" href="#">View All</a>
  </div>
  <div class="cards">
    <article class="card">
      <div class="card-photo" role="img" aria-label="Photo of neighbors talking outdoors" style="background:linear-gradient(135deg,#8fa86a,#5d6b48)"></div>
      <div class="card-body"><h3>Find nearby believers</h3><p>Form fellowships, hold studies, home churches, and participate in activities with church establishments.</p><a class="read-more" href="#">Read More →</a></div>
    </article>
    <article class="card">
      <div class="card-photo" role="img" aria-label="Photo of a woman reading at sunset" style="background:linear-gradient(135deg,#e3b98a,#9c6a44)"></div>
      <div class="card-body"><h3>Share your heart and mind</h3><p>Post your thoughts or publish articles pertaining to the faith, receive feedback from other believers.</p><a class="read-more" href="#">Read More →</a></div>
    </article>
    <article class="card">
      <div class="card-photo" role="img" aria-label="Photo of hands joined in prayer" style="background:linear-gradient(135deg,#f0ddd0,#c9a48c)"></div>
      <div class="card-body"><h3>Meet, grow, and pray together</h3><p>Meet together, online or in person. Praise and worship, serve together. Teach one another, admonish and correct. Pray for one another in love.</p><a class="read-more" href="#">Read More →</a></div>
    </article>
  </div>
</section>

<section class="block testimonial">
  <h2>Testimonial</h2>
  <p class="intro">Many people say that "Sexually immoral for child has to lead that as we Bible already. This is just not true. This is how young professing Christians lose many individuals.</p>
  <a class="arrow" href="#" style="left:192px"><svg width="10" height="12" viewBox="0 0 10 12"><path d="M8 1L2 6l6 5" fill="none" stroke="#333" stroke-width="2"/></svg></a>
  <div class="t-photo" role="img" aria-label="Photo of a man reading a Bible"></div>
  <div class="t-mark">“</div>
  <div class="t-quote">
    <p>Those objectives are primarily to encourage local believers in any neighborhood around the world to read the Bible, be followers first and be present, become disciples, and make disciples, independently of or in complement to the purposes of the established church.</p>
    <div class="t-name">_Mark Ellison</div>
    <div class="t-role">Founder &amp; CEO</div>
  </div>
  <a class="arrow" href="#" style="left:968px"><svg width="10" height="12" viewBox="0 0 10 12"><path d="M2 1l6 5-6 5" fill="none" stroke="#333" stroke-width="2"/></svg></a>
</section>

<footer class="block site-footer">
  <div class="f-brand">
    <span class="brand-name">Hillside Faithful</span>
    <p>Lorem ipsum dolor sit amet, consectetur adipiscing elit, sed do eiusmod tempor incididunt.</p>
    <div class="socials"><span></span><span></span><span></span></div>
  </div>
  <div class="f-col" style="left:500px">
    <h4>Info</h4>
    <ul><li>Home</li><li>Testimonials</li><li>Essentials</li><li>News</li></ul>
  </div>
  <div class="f-col" style="left:620px;top:104px">
    <ul><li>Testimonials</li><li>Privacy policy</li><li>Terms &amp; Condition</li></ul>
  </div>
  <div class="f-col" style="left:800px">
    <h4>Contact</h4>
    <ul>
      <li><svg width="10" height="12" viewBox="0 0 10 12"><path d="M5 11S1 6.5 1 4a4 4 0 018 0c0 2.5-4 7-4 7z" fill="#fff"/></svg>14 Meadow Lane, Fairbrook</li>
      <li><svg width="10" height="10" viewBox="0 0 10 10"><path d="M2 1l2 2-1 1.5a6 6 0 002.5 2.5L7 6l2 2-1.5 1.5C4 9 1 6 .5 2.5z" fill="#fff"/></svg>+01 555 0142</li>
      <li><svg width="12" height="9" viewBox="0 0 12 9"><rect x=".5" y=".5" width="11" height="8" fill="none" stroke="#fff"/><path d="M.5.5L6 5l5.5-4.5" fill="none" stroke="#fff"/></svg>info@hillsidefaithful.example</li>
    </ul>
  </div>
  <div class="copyright">copyright@HillsideFaithful</div>
</footer>

</body>
</html>
```